Poster of Core Values & Motto

Create our core values poster and motto. Attached are our core values and our Motto. This poster represents both of our companies Tidal Pulp & CarvoBin.

Target Market(s)

Our team / employees

Industry/Entity Type

Shredding and Medical Waste

Colors
59FF00
82FF00
B8FF75
E3FFCB
F4FFEA
EB3D1F
EC4F4E
F09395
F8D3D4
FCEDEE

Requirements
Must have
• Include both companies logos

```html
<!DOCTYPE html>
<html lang="en">
<head>
<meta charset="utf-8">
<title>Core Values – Tidal Pulp | CarvoBin</title>
<link rel="stylesheet" href="https://fonts.googleapis.com/css2?family=Open+Sans:wght@400;600&family=Rubik:wght@700;800;900&display=swap">
<style>
  :root {
    --green: #1aab4a;
    --red: #d7262d;
    --ink: #2a2a2a;
    --text: #4a4a4a;
    --frame: #a9a9a9;
    --paper: #f7f7f7;
    --page: #ffffff;
    --dots: #9a9a9a;
  }
  * { box-sizing: border-box; margin: 0; padding: 0; }
  html, body { width: 869px; height: 1200px; overflow: hidden; background: var(--page); }
  .canvas { position: relative; width: 869px; height: 1200px; }
  .poster {
    position: absolute; left: 88px; top: 81px; width: 694px; height: 1040px;
    border: 1px solid var(--frame);
    background: linear-gradient(135deg, #f2f2f2 0%, var(--paper) 40%, #fdfdfd 60%, #f3f3f3 100%);
    overflow: hidden;
    font-family: "Open Sans", sans-serif;
  }
  .waves { position: absolute; left: 0; top: 0; width: 694px; height: 1040px; }
  .abs { position: absolute; }

  .brand { font-family: "Open Sans", sans-serif; font-weight: 600; white-space: nowrap; }
  .brand--pulp { left: 95px; top: 80px; font-size: 38px; color: var(--green); display: flex; align-items: center; gap: 10px; }
  .brand--pulp .mark { width: 26px; height: 26px; border-radius: 50%; background: var(--green); }
  .brand--bin { left: 336px; top: 80px; font-size: 38px; color: var(--red); }
  .brand-divider { left: 312px; top: 79px; width: 1px; height: 62px; background: var(--ink); }

  .title {
    left: 0; width: 694px; top: 190px; text-align: center;
    font-family: "Rubik", sans-serif; font-weight: 900; font-size: 61px; letter-spacing: 1px;
  }
  .title .green { color: var(--green); }
  .title .red { color: var(--red); }

  .value-badge {
    width: 59px; height: 59px; border-radius: 50%;
    background: conic-gradient(var(--red) 0 50%, var(--green) 50% 100%);
    padding: 4px;
    box-shadow: -8px 12px 14px rgba(0,0,0,0.12);
  }
  .value-badge .icon { width: 100%; height: 100%; border-radius: 50%; background: #efefef; border: 3px solid #fff; }

  .value-name { font-family: "Rubik", sans-serif; font-weight: 800; font-size: 20px; color: var(--green); white-space: nowrap; }
  .value-text { font-size: 17px; line-height: 24px; color: var(--text); white-space: nowrap; margin-top: 4px; }
  .rule-dotted { width: 207px; border-top: 1.5px dotted #777; }

  .motto-bar {
    left: 96px; top: 674px; width: 502px; height: 55px;
    background: var(--ink); border-radius: 0 12px 12px 0;
    color: #fff; text-align: center;
    font-family: "Rubik", sans-serif; font-weight: 800; font-size: 35px; line-height: 55px;
    box-shadow: 0 14px 16px -8px rgba(0,0,0,0.3);
  }
  .slogan { left: 0; width: 694px; text-align: center; font-family: "Rubik", sans-serif; font-weight: 800; font-size: 24px; }
  .slogan--green { top: 753px; color: var(--green); }
  .slogan--red { top: 782px; color: var(--red); }
  .rule-solid { left: 119px; top: 825px; width: 455px; border-top: 1.5px solid #999; }
  .web { left: 0; width: 694px; text-align: center; font-family: "Rubik", sans-serif; font-weight: 700; font-size: 21px; color: #555; }
  .web--one { top: 835px; }
  .web--two { top: 867px; }
  .rule-web { left: 241px; top: 863px; width: 212px; border-top: 1.5px dotted #888; }
</style>
</head>
<body>
<div class="canvas">
  <div class="poster">
    <svg class="waves" viewBox="0 0 694 1040" aria-hidden="true">
      <defs>
        <linearGradient id="redFill" x1="0" y1="0" x2="1" y2="0">
          <stop offset="0" stop-color="#d21f27"/><stop offset="1" stop-color="#dc4046"/>
        </linearGradient>
        <linearGradient id="greenFill" x1="0" y1="0" x2="1" y2="0">
          <stop offset="0" stop-color="#2fbf68"/><stop offset="1" stop-color="#0aa447"/>
        </linearGradient>
      </defs>
      <path d="M694 790 C560 905 360 1008 0 1004 L0 1040 L694 1040 Z" fill="url(#redFill)"/>
      <path d="M0 930 C160 985 360 1000 500 922 C380 985 200 1010 0 993 Z" fill="url(#greenFill)"/>
    </svg>

    <div class="abs brand brand--pulp"><span class="mark"></span>Tidal Pulp</div>
    <div class="abs brand-divider"></div>
    <div class="abs brand brand--bin">CarvoBin</div>

    <h1 class="abs title"><span class="green">CORE</span> <span class="red">VALUES</span></h1>

    <div class="abs value-badge" style="left:37px;top:309px"><div class="icon" role="img" aria-label="Teamwork puzzle icon"></div></div>
    <div class="abs" style="left:118px;top:300px">
      <div class="value-name">Synergy/Teamwork</div>
      <div class="value-text">Get It Done Attitude with<br>Humble Confidence</div>
    </div>
    <div class="abs value-badge" style="left:361px;top:309px"><div class="icon" role="img" aria-label="Award badge icon"></div></div>
    <div class="abs" style="left:435px;top:300px">
      <div class="value-name">Excellence</div>
      <div class="value-text">Exceed expectations<br>with a smaile</div>
    </div>
    <div class="abs rule-dotted" style="left:119px;top:398px"></div>
    <div class="abs rule-dotted" style="left:435px;top:398px"></div>

    <div class="abs value-badge" style="left:37px;top:436px"><div class="icon" role="img" aria-label="Hand holding gear icon"></div></div>
    <div class="abs" style="left:118px;top:423px">
      <div class="value-name">Efficient</div>
      <div class="value-text">On-Time, sense of urgency,<br>always trying to improve</div>
    </div>
    <div class="abs value-badge" style="left:361px;top:436px"><div class="icon" role="img" aria-label="Hands holding shield icon"></div></div>
    <div class="abs" style="left:435px;top:423px">
      <div class="value-name">Safe and Secure</div>
      <div class="value-text">We are just as secure as an<br>armored truck with money</div>
    </div>
    <div class="abs rule-dotted" style="left:119px;top:521px"></div>
    <div class="abs rule-dotted" style="left:435px;top:521px"></div>

    <div class="abs value-badge" style="left:37px;top:549px"><div class="icon" role="img" aria-label="Process gear icon"></div></div>
    <div class="abs" style="left:118px;top:548px">
      <div class="value-name">Honesty/Intergrity</div>
      <div class="value-text">Do the right thing</div>
    </div>
    <div class="abs value-badge" style="left:361px;top:549px"><div class="icon" role="img" aria-label="Team members icon"></div></div>
    <div class="abs" style="left:435px;top:548px">
      <div class="value-name">Dependable</div>
      <div class="value-text">Do what you say you will do</div>
    </div>

    <div class="abs motto-bar">Purpose/Cause/Passion</div>
    <div class="abs slogan slogan--green">REMIND PEOPLE</div>
    <div class="abs slogan slogan--red">WHAT GREAT SERVICE LOOKS LIKE</div>
    <div class="abs rule-solid"></div>
    <div class="abs web web--one">www.tidalpulp.com</div>
    <div class="abs rule-web"></div>
    <div class="abs web web--two">www.carvobin.com</div>
  </div>
</div>
</body>
</html>
```